Brindle Logistics Business Card Design

We are a trucking and warehousing company. We run freight in the US manly from the Pacific NW to TX and back up the the PNW. We also do warehousing where we store, move, and distribute freight. Looking for a clean and modern design of business card. We would like to look rich and elegant. Attached is our logo.

Industry/Entity Type

Trucking Company

Contact Information for Business Card

Looking for a clean and modern design of business card. We would like to look rich and elegant.

Font styles to use
Sans Serif

Colors

Designer to choose colors to be used in the design.

Requirements
Must have
• logo but it should not dominate the card
Should not have
• logo should not dominate the card

```html
<!DOCTYPE html>
<html lang="en">
<head>
<meta charset="utf-8">
<title>Brindle Logistics Business Card</title>
<link href="https://fonts.googleapis.com/css2?family=Montserrat:wght@500;600;700&display=swap" rel="stylesheet">
<style>
  :root {
    --backdrop: #2b2b2b;
    --card: #f4f4f4;
    --ink: #3a3a3c;
    --ink-soft: #55575a;
    --brand-blue: #1f6fb2;
    --band-dark: #3b3b3d;
    --band-text: #e6e6e6;
  }
  * { box-sizing: border-box; margin: 0; padding: 0; }
  html, body {
    width: 1200px; height: 997px; overflow: hidden;
    background: var(--backdrop);
    font-family: "Montserrat", Arial, sans-serif;
  }
  .stage { position: relative; width: 1200px; height: 997px; }
  .card {
    position: absolute; width: 540px; height: 308px;
    background: var(--card); border-radius: 3px; overflow: hidden;
    box-shadow: 0 14px 30px rgba(0,0,0,.45);
  }
  /* front */
  .card--front { left: 70px; top: 130px; }
  .front-brand {
    position: absolute; left: 70px; top: 92px;
    display: flex; align-items: center; gap: 22px;
  }
  .brand-dot { width: 92px; height: 92px; border-radius: 50%; background: var(--brand-blue); flex: none; }
  .brand-name {
    color: var(--ink); font-weight: 600; text-transform: uppercase;
    letter-spacing: 1px; line-height: 1.05;
  }
  .front-brand .brand-name { font-size: 34px; }
  .front-web {
    position: absolute; left: 184px; top: 222px;
    font-size: 13px; font-weight: 600; color: var(--ink-soft); letter-spacing: .5px;
  }
  /* back */
  .card--back { left: 590px; top: 430px; }
  .back-brand { position: absolute; right: 36px; top: 40px; text-align: right; }
  .back-brand .brand-name { font-size: 32px; }
  .band-contact {
    position: absolute; left: 270px; top: 150px; width: 270px; height: 82px;
    background: var(--band-dark); padding: 12px 0 0 68px;
  }
  .contact-list { list-style: none; }
  .contact-list li {
    display: flex; align-items: center; gap: 8px;
    color: var(--band-text); font-size: 11px; font-weight: 500; height: 20px;
    white-space: nowrap;
  }
  .contact-list svg { width: 13px; height: 13px; flex: none; }
  .band-person {
    position: absolute; left: 0; top: 202px; width: 270px; height: 58px;
    background: var(--brand-blue); padding: 12px 0 0 30px; color: #fff;
  }
  .person-name { font-size: 13px; font-weight: 700; text-transform: uppercase; letter-spacing: .3px; white-space: nowrap; }
  .person-role { font-size: 12px; font-weight: 500; margin: 2px 0 0 92px; }
  .back-seal {
    position: absolute; left: 212px; top: 146px; width: 116px; height: 116px;
    border-radius: 50%; background: var(--card); border: 3px solid var(--band-dark);
  }
  .back-web {
    position: absolute; left: 200px; top: 274px;
    font-size: 14px; font-weight: 700; color: var(--ink); letter-spacing: .5px;
  }
</style>
</head>
<body>
<main class="stage">
  <section class="card card--front">
    <div class="front-brand">
      <span class="brand-dot"></span>
      <span class="brand-name">Brindle<br>Logistics, LLC</span>
    </div>
    <p class="front-web">www.brindlefreight.com</p>
  </section>

  <section class="card card--back">
    <div class="back-brand">
      <span class="brand-name">Brindle<br>Logistics, LLC</span>
    </div>
    <div class="band-person">
      <p class="person-name">Mrs Elena Marwood</p>
      <p class="person-role">Director</p>
    </div>
    <div class="band-contact">
      <ul class="contact-list">
        <li>
          <svg viewBox="0 0 14 14"><circle cx="7" cy="7" r="7" fill="#1f6fb2"/><path d="M4 5.5c0-1 1-1.5 3-1.5s3 .5 3 1.5v.5H8.5v-.7h-3V6H4z M4.5 7h5l.5 3H4z" fill="#fff"/></svg>
          02 5550 1234
        </li>
        <li>
          <svg viewBox="0 0 14 14"><circle cx="7" cy="7" r="7" fill="#1f6fb2"/><rect x="5" y="3" width="4" height="8" rx="1" fill="#fff"/></svg>
          0400 555 217
        </li>
        <li>
          <svg viewBox="0 0 14 14"><circle cx="7" cy="7" r="7" fill="#1f6fb2"/><rect x="3.5" y="4.5" width="7" height="5" fill="#fff"/><path d="M3.5 4.5 7 7.5l3.5-3" fill="none" stroke="#1f6fb2" stroke-width=".8"/></svg>
          elena@brindlefreight.com
        </li>
      </ul>
    </div>
    <span class="back-seal"></span>
    <p class="back-web">www.brindlefreight.com</p>
  </section>
</main>
</body>
</html>
```